Create a pouch design for a new sports supplement product

Dimensions are 235mm (width) x 335mm (length) x 110mm (gusset)
File 1 - Extension of design brief please read both briefs
File 2 - Is 2 potential pouches this is just to give you a better example of size the dimensions are for the pouch on the right. This picture is not to give you design ideas as I am not very keen on either of these designs.
We need a design to be printed onto the pouches of our whey protein product. The brand name is 'Stellar Fuelworks' and needs to be displayed on the packaging either just writing or a simple logo design. I am not the most creative person in the world but have put together a more detailed brief listing some of the key information that needs to be included on the pouch (See attachment) Please feel free if you have experience of this the sports supplement market or have different ideas then please feel free to explore them.
The pouch would either be printed straight onto the pouch, or possibly just a printed label (front & back) to be stuck onto the pouch. Please design either or both.
Open to different colour schemes. Design has to be modern looking and eye-catching.
Some key points;
High quality whey protein concentrate
All Natural
Soy free
Great tasting
Please google image search 'protein pouches' to see other designs if your not familiar with the sports supplement market.
Any questions feel free to ask.
Updates
Hi, Thanks for all your design! I am really busy at the moment so haven't had chance to give feedback and have a proper look through all the designs. I have extended the time frame to give myself chance to give proper feedback and see any changes needed. Expect feedback sunday at the latest, and I will be pick a design early next week.
Target Market(s)
Sports supplement market. Product is a whey protein shake
Industry/Entity Type
Nutrition
Look and feel
Each slider illustrates characteristics of the customer's brand and the style your logo design should communicate.

```html
<!DOCTYPE html>
<html lang="en">
<head>
<meta charset="utf-8">
<title>Stellar Fuelworks – Natural Whey Protein Pouch</title>
<link rel="stylesheet" href="https://fonts.googleapis.com/css2?family=Montserrat:wght@700;800&family=Roboto+Condensed:wght@500&family=Roboto:wght@500&display=swap">
<style>
  :root {
    --stage: #c8c8c8;
    --pouch: #262626;
    --band: #3a3a3a;
    --lime: #8fd21c;
    --lime-light: #c5ea20;
    --green: #6cbf1f;
    --ink: #1e1e1e;
    --white: #ffffff;
    --berry: #d9184a;
    --badge: #d2d2d2;
  }
  * { margin: 0; padding: 0; box-sizing: border-box; }
  html, body { width: 1002px; height: 1200px; overflow: hidden; }
  body { background: var(--stage); position: relative; font-family: "Montserrat", sans-serif; }
  .pouch {
    position: absolute; left: 81px; top: 10px; width: 840px; height: 1180px;
    background: var(--pouch); overflow: hidden;
  }
  .tear-line { position: absolute; left: 0; right: 0; top: 32px; border-top: 2px dashed var(--green); }
  .tear-label {
    position: absolute; right: 30px; top: 38px; color: var(--white);
    font-family: "Roboto", sans-serif; font-weight: 500; font-size: 12px;
  }
  .swoosh { position: absolute; left: 0; top: 120px; width: 840px; height: 400px; }
  .brand {
    position: absolute; left: 210px; top: 212px; color: var(--ink);
    font-weight: 800; text-transform: uppercase; line-height: 1;
  }
  .brand-top { display: block; font-size: 96px; letter-spacing: 1px; }
  .brand-bottom { display: block; font-size: 60px; margin-top: 8px; letter-spacing: 1px; }
  .hex { position: absolute; width: 88px; height: 100px; }
  .hex-amino { left: 262px; top: 515px; }
  .hex-training { left: 182px; top: 617px; }
  .hex-leaf { left: 264px; top: 716px; }
  .product-name {
    position: absolute; left: 392px; top: 602px; padding-left: 18px;
    border-left: 5px solid var(--green); color: var(--white);
    font-weight: 800; font-size: 37px; line-height: 47px; text-transform: uppercase;
  }
  .flavour {
    position: absolute; left: 392px; top: 766px; width: 228px; height: 42px;
    background: var(--berry); clip-path: polygon(0 0, 90% 0, 100% 50%, 90% 100%, 0 100%);
    color: var(--white); padding: 3px 0 0 18px; line-height: 1;
  }
  .flavour-name { display: block; font-weight: 800; font-size: 19px; }
  .flavour-label { display: block; font-family: "Roboto", sans-serif; font-size: 12px; letter-spacing: 2px; margin-top: 2px; }
  .badge { position: absolute; left: 130px; top: 855px; width: 170px; height: 170px; }
  .benefits { position: absolute; left: 390px; top: 872px; list-style: none; }
  .benefits li {
    width: 390px; height: 30px; margin-bottom: 10px; background: var(--green);
    color: var(--white); font-family: "Roboto Condensed", sans-serif; font-weight: 500;
    font-size: 17px; line-height: 30px; padding-left: 14px; text-transform: uppercase;
  }
  .servings { position: absolute; left: 164px; top: 1088px; color: var(--white); line-height: 1; }
  .servings-count { display: block; font-weight: 800; font-size: 46px; }
  .servings-count .accent { color: var(--green); }
  .servings-label { display: block; font-family: "Roboto", sans-serif; font-size: 12px; letter-spacing: 2px; }
  .net-weight {
    position: absolute; left: 668px; top: 1102px; color: var(--white);
    font-family: "Roboto", sans-serif; font-weight: 500; font-size: 26px;
  }
</style>
</head>
<body>
<main class="pouch">
  <div class="tear-line"></div>
  <div class="tear-label">TEAR HERE &amp; RESEAL</div>

  <svg class="swoosh" viewBox="0 0 840 400" aria-hidden="true">
    <defs>
      <linearGradient id="limeGlow" x1="0" y1="0" x2="1" y2="1">
        <stop offset="0" stop-color="var(--lime)"/>
        <stop offset="1" stop-color="var(--lime-light)"/>
      </linearGradient>
    </defs>
    <path d="M0 250 C120 80 420 10 840 60 L840 200 C640 420 220 420 0 330 Z" fill="var(--band)"/>
    <path d="M80 190 C200 70 480 20 820 80 C700 280 430 360 250 330 C170 310 110 260 80 190 Z" fill="url(#limeGlow)"/>
  </svg>

  <h1 class="brand">
    <span class="brand-top">Stellar</span>
    <span class="brand-bottom">Fuelworks</span>
  </h1>

  <svg class="hex hex-amino" viewBox="0 0 88 100" role="img" aria-label="Amino acid molecule icon">
    <polygon points="44,0 88,25 88,75 44,100 0,75 0,25" fill="var(--green)"/>
  </svg>
  <svg class="hex hex-training" viewBox="0 0 88 100" role="img" aria-label="Photo of an arm lifting a dumbbell">
    <polygon points="44,0 88,25 88,75 44,100 0,75 0,25" fill="#b9a59a"/>
  </svg>
  <svg class="hex hex-leaf" viewBox="0 0 88 100" role="img" aria-label="Natural leaf icon">
    <polygon points="44,0 88,25 88,75 44,100 0,75 0,25" fill="var(--green)"/>
  </svg>

  <h2 class="product-name">Natural<br>Whey<br>Protein</h2>

  <div class="flavour">
    <span class="flavour-name">STRAWBERRY</span>
    <span class="flavour-label">FLAVOUR</span>
  </div>

  <svg class="badge" viewBox="0 0 170 170" aria-hidden="true">
    <circle cx="85" cy="85" r="82" fill="var(--badge)"/>
  </svg>

  <ul class="benefits">
    <li>No artificial flavours</li>
    <li>Excellent amino acid profile</li>
    <li>80% high quality protein content</li>
    <li>Soy free</li>
  </ul>

  <div class="servings">
    <span class="servings-count">3<span class="accent">0</span></span>
    <span class="servings-label">SERVINGS</span>
  </div>

  <div class="net-weight">909g</div>
</main>
</body>
</html>
```